Brand new website for global research and investment startup

We need a simple website, maybe 3 pages: landing page with business description, investment philosophy, team and contact info.
We have a logo already that can be incorporated. Please use the logo only, not the text
We like the color green, something along the lines of #3D6C32 as the main color.
We'd like to design the website with geometric shapes in gradations of the base color. The shapes should suggest "work in progress", "built to last (a long time)", "solidity" and "indestructibility". One idea floating in my head sees smaller features with icosahedron and dodecahedron shapes, and maybe larger structures like crystal lattices; but please feel free to be creative and imagine your own.

```html
<!DOCTYPE html>
<html lang="en">
<head>
<meta charset="utf-8">
<title>Ridgeline Research Investment</title>
<link href="https://fonts.googleapis.com/css2?family=Manrope:wght@500;600;700;800&family=Inter:wght@400;500;600&display=swap" rel="stylesheet">
<style>
:root{
  --green:#3D6C32;
  --green-bright:#4c8a3c;
  --green-dark:#2a5a30;
  --green-deep:#1f4a28;
  --ink:#1d1d1d;
  --muted:#555a55;
  --tint:#eef5ec;
  --tint-2:#dcebd7;
  --white:#ffffff;
}
*{box-sizing:border-box;margin:0;padding:0}
html,body{width:1200px;height:4478px;overflow:hidden}
body{position:relative;background:var(--white);font-family:"Inter",sans-serif;color:var(--ink)}
h1,h2,h3,h4,.brand{font-family:"Manrope",sans-serif}

/* header */
.site-header{position:absolute;left:0;top:0;width:1200px;height:87px;border-bottom:1px solid #e6ebe5;background:var(--white)}
.brand{position:absolute;left:120px;top:28px;display:flex;align-items:center;gap:10px;font-weight:800;font-size:20px;color:var(--green)}
.brand-dot{width:22px;height:22px;border-radius:50%;background:var(--green)}
.main-nav{position:absolute;left:447px;top:36px;display:flex;gap:25px;font-size:12px;font-weight:600;letter-spacing:.3px}
.main-nav a{color:var(--ink);text-decoration:none}
.main-nav a.active{color:var(--green-bright)}
.btn-start{position:absolute;left:929px;top:26px;width:151px;height:35px;border-radius:18px;background:linear-gradient(90deg,var(--green-dark),var(--green-bright));color:#fff;font-size:11px;font-weight:700;display:flex;align-items:center;justify-content:center;gap:10px;letter-spacing:.3px}

/* hero */
.hero{position:absolute;left:0;top:88px;width:1200px;height:1350px;background:radial-gradient(ellipse 420px 380px at 1150px 60px,#cfe5c9 0%,rgba(255,255,255,0) 100%),radial-gradient(ellipse 380px 500px at 20px 900px,#d6ead0 0%,rgba(255,255,255,0) 100%),#fbfdfa}
.eyebrow{font-size:15px;font-weight:500;color:var(--green);letter-spacing:.6px}
.hero .eyebrow{position:absolute;left:0;top:68px;width:1200px;text-align:center}
.hero h1{position:absolute;left:0;top:100px;width:1200px;text-align:center;font-size:40px;line-height:45px;font-weight:600;color:var(--ink)}
.hero p{position:absolute;left:0;top:200px;width:1200px;text-align:center;font-size:12px;line-height:20px;color:var(--muted)}
.btn-learn{position:absolute;left:501px;top:265px;width:198px;height:54px;border-radius:27px;background:linear-gradient(90deg,var(--green-dark),var(--green-bright));color:#fff;font-size:14px;font-weight:700;display:flex;align-items:center;justify-content:center;gap:14px;letter-spacing:.5px}
.hero-photo{position:absolute;left:120px;top:376px;width:960px;height:545px;border-radius:52px;background:linear-gradient(110deg,#c9cfc6 0%,#8d9589 35%,#3c4452 55%,#b9b7b0 75%,#b88a65 100%)}
.hero-frame{position:absolute;left:148px;top:402px;width:904px;height:493px;border:2px dashed rgba(255,255,255,.9);border-radius:40px}

.value{position:absolute;width:300px;text-align:center}
.value .ring{width:126px;height:126px;margin:0 auto;border-radius:50%;border:6px solid var(--green);display:flex;align-items:center;justify-content:center;background:#fff}
.value h3{margin-top:24px;font-size:20px;font-weight:700;letter-spacing:.5px}
.value p{margin-top:8px;font-size:11.5px;line-height:17px;color:var(--muted)}
.divider-v{position:absolute;top:1089px;width:1px;height:281px;background:#dfe6dd}

/* who we are */
.about{position:absolute;left:0;top:1440px;width:1200px;height:403px;background:linear-gradient(90deg,#f1f7ef,#f7fbf6)}
.about .eyebrow{position:absolute;left:120px;top:74px;font-size:13px;color:var(--green-bright)}
.about h2{position:absolute;left:120px;top:102px;font-size:38px;line-height:44px;font-weight:700;color:var(--green-dark)}
.about .lead{position:absolute;left:610px;top:70px;width:415px;font-size:12.5px;line-height:21px;font-weight:600;color:#2a2a2a}
.about .body{position:absolute;left:610px;top:150px;width:415px;font-size:12.5px;line-height:21px;color:#444}
.btn-outline{position:absolute;left:610px;top:283px;width:214px;height:48px;border-radius:24px;border:1.5px solid var(--green);color:var(--green-dark);font-size:12.5px;font-weight:600;display:flex;align-items:center;justify-content:center;gap:10px;background:#fff}

/* philosophy */
.philosophy{position:absolute;left:0;top:1843px;width:1200px;height:823px;background:radial-gradient(ellipse 600px 300px at 620px 100px,#deeed9 0%,rgba(255,255,255,0) 100%),radial-gradient(ellipse 500px 600px at 1200px 700px,#d3e8cd 0%,rgba(255,255,255,0) 100%),#fbfdfa}
.philosophy .eyebrow{position:absolute;left:0;top:70px;width:1200px;text-align:center;font-size:14px;color:var(--green-bright)}
.philosophy h2{position:absolute;left:0;top:103px;width:1200px;text-align:center;font-size:38px;line-height:44px;font-weight:600;color:var(--green-dark)}
.philosophy-photo{position:absolute;left:120px;top:230px;width:463px;height:520px;border-radius:30px;background:linear-gradient(180deg,#9fbbd8 0%,#d8e3ec 45%,#e8eef0 78%,#7fb04a 82%,#5f9a34 100%)}
.principle{position:absolute;left:631px;width:449px}
.principle .num{display:inline-block;padding:3px 6px;border-radius:5px;background:#dfeedb;color:var(--green);font-size:12px;font-weight:600}
.principle h3{margin-top:14px;font-size:20px;font-weight:700;letter-spacing:.3px}
.principle p{margin-top:6px;font-size:11px;line-height:17px;color:#555}
.rule{position:absolute;left:631px;width:449px;height:1px;background:#d4dcd2}

/* quote */
.credo{position:absolute;left:0;top:2666px;width:1200px;height:278px;background:var(--green-dark);color:#fff;text-align:center}
.credo blockquote{position:absolute;left:0;top:64px;width:1200px;font-family:"Manrope",sans-serif;font-size:37px;line-height:46px;font-weight:500}
.credo cite{position:absolute;left:0;top:185px;width:1200px;display:block;text-align:center;font-style:normal;font-size:11px;font-weight:600;letter-spacing:.4px}

/* team */
.team-title{position:absolute;left:0;top:3007px;width:1200px;text-align:center;font-size:38px;font-weight:600;color:var(--green-dark)}
.portrait{position:absolute;left:120px;width:480px;height:358px;border-radius:30px}
.portrait.one{top:3085px;background:linear-gradient(90deg,#c7cfc2,#6a7262 40%,#2c2f36 60%,#a7b1a4)}
.portrait.two{top:3568px;background:linear-gradient(90deg,#8f8b84,#3a3c40 45%,#25272c 65%,#c9c6c0)}
.member-name{position:absolute;left:120px;width:480px;text-align:center;font-family:"Manrope",sans-serif;font-size:24px;font-weight:600}
.member-role{position:absolute;left:120px;width:480px;text-align:center;font-size:12px;font-weight:600;color:var(--green);letter-spacing:.5px}
.bio{position:absolute;left:640px;width:412px;font-size:12.5px;line-height:21px;color:#555;text-align:justify}
.bio p+p{margin-top:21px}

/* footer */
.site-footer{position:absolute;left:0;top:4075px;width:1200px;height:363px;background:linear-gradient(90deg,#f4f8f3,#f7faf6)}
.footer-brand{position:absolute;left:120px;top:80px;display:flex;align-items:center;gap:10px;font-family:"Manrope",sans-serif;font-weight:800;font-size:19px;color:var(--green-dark)}
.footer-brand .brand-dot{background:var(--green-dark)}
.footer-about{position:absolute;left:120px;top:144px;width:300px;font-size:11.5px;line-height:19px;color:#555}
.social{position:absolute;top:216px;width:30px;height:30px;border-radius:50%;background:var(--green-bright)}
.footer-head{position:absolute;top:70px;font-family:"Manrope",sans-serif;font-size:15px;font-weight:600;letter-spacing:.3px}
.footer-head::after{content:"";display:block;width:28px;height:2px;background:var(--green-dark);margin-top:8px}
.footer-nav{position:absolute;left:558px;top:127px;list-style:none;font-size:11.5px}
.footer-nav li{height:29.6px;padding-left:20px;position:relative}
.footer-nav li::before{content:"";position:absolute;left:4px;top:6px;width:4px;height:4px;border-radius:50%;background:#333}
.contact-item{position:absolute;left:854px;display:flex;gap:12px;font-size:11.5px;line-height:17px;color:#222}
.contact-item svg{flex:none;margin-top:2px}
.bottom-bar{position:absolute;left:0;top:4438px;width:1200px;height:40px;background:var(--green-dark);color:#fff;font-size:11.5px;display:flex;align-items:center;justify-content:center}
</style>
</head>
<body>

<header class="site-header">
  <div class="brand"><span class="brand-dot"></span>Ridgeline</div>
  <nav class="main-nav">
    <a class="active" href="#">HOME</a><a href="#">PHILOSOPHY</a><a href="#">INSIGHTS</a><a href="#">BLOG</a><a href="#">TEAM</a><a href="#">CONTACT</a>
  </nav>
  <div class="btn-start">GET STARTED
    <svg width="8" height="10" viewBox="0 0 8 10"><path d="M2 1l4 4-4 4" fill="none" stroke="#fff" stroke-width="1.6"/></svg>
  </div>
</header>

<section class="hero">
  <div class="eyebrow">WELCOME TO</div>
  <h1>OUR RELATIONAL<br>APPROACH TO GROWTH</h1>
  <p>We believe in stewardship, not just transactions. By fostering deep, participatory relationships,<br>we cultivate long-term stability and organic growth for our partners.</p>
  <div class="btn-learn">LEARN MORE
    <svg width="9" height="12" viewBox="0 0 9 12"><path d="M2 1l5 5-5 5" fill="none" stroke="#fff" stroke-width="1.8"/></svg>
  </div>
  <div class="hero-photo" role="img" aria-label="Photo of two colleagues reviewing documents beside a laptop in a bright office"></div>
  <div class="hero-frame"></div>
</section>

<div class="value" style="left:121px;top:1097px">
  <div class="ring"><svg width="64" height="64" viewBox="0 0 64 64" fill="none" stroke="#3D6C32" stroke-width="3.5" stroke-linejoin="round"><path d="M32 54 10 32a12 12 0 0 1 17-17l5 5 5-5a12 12 0 0 1 17 17Z"/><path d="M22 34l8 8M28 30l8 8M34 26l8 8"/></svg></div>
  <h3>INTEGRITY</h3>
  <p>Lorem ipsum dolor sit amet consectetur<br>adipiscing elit, sed do eiusmod tempor<br>incididunt magna aliqua.</p>
</div>
<div class="divider-v" style="left:433px"></div>
<div class="value" style="left:448px;top:1097px">
  <div class="ring"><svg width="64" height="64" viewBox="0 0 64 64" fill="none" stroke="#3D6C32" stroke-width="3.5"><circle cx="27" cy="30" r="17"/><circle cx="37" cy="34" r="17"/></svg></div>
  <h3>TRANSPARENCY</h3>
  <p>Lorem ipsum dolor sit amet consectetur<br>adipiscing elit, sed do eiusmod tempor<br>incididunt magna aliqua.</p>
</div>
<div class="divider-v" style="left:763px"></div>
<div class="value" style="left:777px;top:1097px">
  <div class="ring"><svg width="64" height="64" viewBox="0 0 64 64" fill="none" stroke="#3D6C32" stroke-width="3.5"><path d="M8 54h48M14 54V40h7v14M27 54V32h7v22M40 54V24h7v30"/><path d="M12 34 28 20l8 6 16-14M44 12h8v8"/></svg></div>
  <h3>EFFICIENCY</h3>
  <p>Lorem ipsum dolor sit amet consectetur<br>adipiscing elit, sed do eiusmod tempor<br>incididunt magna aliqua.</p>
</div>

<section class="about">
  <div class="eyebrow">WHO WE ARE</div>
  <h2>WE INVEST IN THE<br>FUTURES THAT<br>MATTER MOST.</h2>
  <p class="lead">Stonefield Partners is a private investment firm built on the conviction that lasting financial success and meaningful human relationships are not in tension — they are inseparable.</p>
  <p class="body">We work with a small number of carefully selected families, foundations, and professional investors — investing side by side across private equity, real assets, and long-term growth companies. No mass-marketing. Only face-to-face relationships built on trust.</p>
  <div class="btn-outline">Learn how we invest
    <svg width="7" height="10" viewBox="0 0 7 10"><path d="M1.5 1l4 4-4 4" fill="none" stroke="#2a5a30" stroke-width="1.6"/></svg>
  </div>
</section>

<section class="philosophy">
  <div class="eyebrow">INVESTMENT PHILOSOPHY</div>
  <h2>THREE PRINCIPLES.<br>ONE ENDURING BELIEF.</h2>
  <div class="philosophy-photo" role="img" aria-label="Photo of a handshake against a blue sky above a green field"></div>
</section>
<div class="principle" style="top:2100px">
  <span class="num">01</span>
  <h3>PATIENT CAPITAL</h3>
  <p>We invest for generations, not quarters. The most meaningful growth happens on a horizon measured in decades, not earnings cycles. Our positions are held for 7 to 15 years — or longer, when a business warrants it.</p>
</div>
<div class="rule" style="top:2243px"></div>
<div class="principle" style="top:2278px">
  <span class="num">02</span>
  <h3>SHARED JOURNEY</h3>
  <p>We invest alongside every client. When we recommend an opportunity, our own capital is already committed. This alignment is non-negotiable — it ensures our interests remain perfectly matched at every stage.</p>
</div>
<div class="rule" style="top:2421px"></div>
<div class="principle" style="top:2455px">
  <span class="num">03</span>
  <h3>PURPOSEFUL GROWTH</h3>
  <p>Capital should serve life. Every investment we make considers its effect on people, communities, and the natural world. We believe the most enduring value is created by companies that make things genuinely better.</p>
</div>

<section class="credo">
  <blockquote>"The most important investments are the<br>ones that outlast the investor."</blockquote>
  <cite>STONEFIELD PARTNERS · INVESTMENT CREDO</cite>
</section>

<h2 class="team-title">THE TEAM</h2>
<div class="portrait one" role="img" aria-label="Portrait photo of a senior partner in a dark suit"></div>
<div class="member-name" style="top:3469px">ARTHUR VALE</div>
<div class="member-role" style="top:3508px">PARTNER</div>
<div class="bio" style="top:3113px">
  <p>Lorem ipsum dolor sit amet, consectetur adipisicing elit, sed do eiusmod tempor incididunt ut labore et dolore magna aliqua. Ut enim ad minim veniam, quis nostrud exercitation ullamco laboris nisi ut aliquip ex ea commodo consequat.</p>
  <p>Duis aute irure dolor in reprehenderit in voluptate velit esse cillum dolore eu fugiat nulla pariatur. Excepteur sint occaecat cupidatat non proident, sunt in culpa qui officia deserunt mollit anim id est laborum. Sed ut perspiciatis unde omnis iste natus error sit voluptatem accusantium doloremque laudantium, totam rem aperiam, eaque ipsa quae ab illo inventore veritatis et quasi architecto beatae vitae dicta sunt explicabo. Nemo enim ipsam voluptatem quia voluptas sit aspernatur aut odit aut fugit, sed quia consequuntur magni dolores eos qui ratione.</p>
</div>

<div class="portrait two" role="img" aria-label="Portrait photo of a partner in a dark suit and tie"></div>
<div class="member-name" style="top:3953px">MARCUS HALE</div>
<div class="member-role" style="top:3991px">PARTNER</div>
<div class="bio" style="top:3597px">
  <p>Lorem ipsum dolor sit amet, consectetur adipisicing elit, sed do eiusmod tempor incididunt ut labore et dolore magna aliqua. Ut enim ad minim veniam, quis nostrud exercitation ullamco laboris nisi ut aliquip ex ea commodo consequat.</p>
  <p>Duis aute irure dolor in reprehenderit in voluptate velit esse cillum dolore eu fugiat nulla pariatur. Excepteur sint occaecat cupidatat non proident, sunt in culpa qui officia deserunt mollit anim id est laborum. Sed ut perspiciatis unde omnis iste natus error sit voluptatem accusantium doloremque laudantium, totam rem aperiam, eaque ipsa quae ab illo inventore veritatis et quasi architecto beatae vitae dicta sunt explicabo. Nemo enim ipsam voluptatem quia voluptas sit aspernatur aut odit aut fugit, sed quia consequuntur magni dolores eos qui ratione.</p>
</div>

<footer class="site-footer">
  <div class="footer-brand"><span class="brand-dot"></span>RIDGELINE</div>
  <p class="footer-about">Ridgeline research investment is a private investment firm for select families and institutions. Geneva — by appointment only.</p>
  <span class="social" style="left:121px"></span>
  <span class="social" style="left:156px"></span>
  <span class="social" style="left:190px"></span>
  <span class="social" style="left:225px"></span>

  <div class="footer-head" style="left:558px">NAVIGATE</div>
  <ul class="footer-nav">
    <li>HOME</li><li>PHILOSOPHY</li><li>INSIGHTS</li><li>BLOG</li><li>TEAM</li><li>CONTACT</li>
  </ul>

  <div class="footer-head" style="left:854px">CONTACT US</div>
  <div class="contact-item" style="top:129px">
    <svg width="11" height="14" viewBox="0 0 11 14"><path d="M5.5 0A5.5 5.5 0 0 0 0 5.5C0 9.5 5.5 14 5.5 14S11 9.5 11 5.5A5.5 5.5 0 0 0 5.5 0Zm0 7.5a2 2 0 1 1 0-4 2 2 0 0 1 0 4Z" fill="#2a5a30"/></svg>
    <span>1420 Cedar Row #210<br>Stillwater, NV 89000</span>
  </div>
  <div class="contact-item" style="top:180px">
    <svg width="12" height="12" viewBox="0 0 12 12"><path d="M2.5 0 4.5 2.5 3.5 4a7 7 0 0 0 4.5 4.5L9.5 7.5 12 9.5 10.5 12C5 12 0 7 0 1.5Z" fill="#2a5a30"/></svg>
    <span>+88 555 010 200</span>
  </div>
  <div class="contact-item" style="top:217px">
    <svg width="13" height="10" viewBox="0 0 13 10"><rect width="13" height="10" rx="1" fill="#2a5a30"/><path d="M1 1l5.5 4.5L12 1" fill="none" stroke="#fff" stroke-width="1.2"/></svg>
    <span>hello@ridgelineresearch.example</span>
  </div>
</footer>
<div class="bottom-bar">© 2024 Ridgeline Research Investment. All rights reserved.</div>

</body>
</html>
```